Werbetafel für Immobilienverwaltung
Zielgruppe
Wir sind im Kern eine Immobilienverwaltung, daher richten wir uns an Eigentümer/Investoren/Kapitalanleger. Neben der Verwaltung welche auch durch Hausmeisterservice (Grünarbeiten usw.) erweitert werden kann, bieten wir die Gutachtenerstellung sowie den Vertrieb (Maklertätigkeit in Verkauf sowie Vermietung) an.
Ein großer Vorteil ist unsere Digitale Arbeitsweise (noch keine Selbstverständlichkeit in der Branche).
Aufgabenstellung
Ziel ist es, das Unternehmen unaufdringlich jedoch wirksam und informativ auf einer Werbetafel zu präsentieren.
Maße der Tafel, welche sich im ausgangsbereich eines großen Lebensmittelunternehmens befindet, ist B 320cm x H 120cm.
Die Kundschaft läuft in ca. 1m Entfernung an der Tafel vorbei, sie sollte also von nahem nicht zu überrumpelt wirken.
Unser Logo sowie Telefonnummer sollte iwie untergebracht werden.
Gern auch eigene Ideen umsetzen falls Ihr welche habt.

```html
<!DOCTYPE html>
<html lang="de">
<head>
<meta charset="utf-8">
<title>Nordhaus Immobilien – Werbetafel</title>
<link rel="stylesheet" href="https://fonts.googleapis.com/css2?family=Poppins:wght@400;600;700&display=swap">
<style>
  :root {
    --brand-red: #8b2229;
    --stripe-grey: #e4e4e4;
    --text-grey: #5f5f5f;
    --rule-grey: #9a9a98;
    --phone-pink: #f28a8e;
    --white: #ffffff;
    --canvas-bg: #eef0f2;
  }
  * { margin: 0; padding: 0; box-sizing: border-box; }
  html, body {
    width: 1200px; height: 1117px; overflow: hidden;
    background: var(--canvas-bg);
    font-family: "Poppins", Arial, sans-serif;
  }
  .billboard {
    position: absolute; left: 0; top: 333px;
    width: 1200px; height: 450px;
    background: var(--white);
    overflow: hidden;
  }
  .billboard__shapes { position: absolute; inset: 0; width: 1200px; height: 450px; }
  .brand {
    position: absolute; left: 66px; top: 148px;
    font-weight: 600; font-size: 50px; line-height: 1;
    color: var(--brand-red); letter-spacing: -0.5px; white-space: nowrap;
  }
  .brand__rule {
    position: absolute; left: 66px; top: 211px;
    width: 582px; height: 2px; background: var(--rule-grey);
  }
  .tagline {
    position: absolute; left: 193px; top: 226px;
    font-weight: 400; font-size: 17px; letter-spacing: 0.6px;
    color: var(--text-grey); white-space: nowrap;
  }
  .contact__phone {
    position: absolute; left: 176px; top: 305px;
    font-weight: 700; font-size: 70px; line-height: 1;
    color: var(--white); letter-spacing: -0.5px; white-space: nowrap;
  }
  .contact__phone-icon { position: absolute; left: 104px; top: 316px; width: 112px; height: 112px; }
  .contact__web-icon { position: absolute; left: 240px; top: 391px; width: 28px; height: 28px; }
  .contact__web {
    position: absolute; left: 279px; top: 388px;
    font-weight: 700; font-size: 27px; line-height: 1.2;
    color: var(--white); white-space: nowrap;
  }
  .services {
    position: absolute; left: 816px; top: 326px;
    color: var(--brand-red);
  }
  .services__title {
    font-weight: 700; font-size: 26px; line-height: 31px; letter-spacing: -0.2px;
  }
  .services__claim {
    margin-top: 4px; font-weight: 400; font-size: 15.5px; letter-spacing: 0.2px;
  }
</style>
</head>
<body>
  <section class="billboard">
    <svg class="billboard__shapes" viewBox="0 0 1820 682" preserveAspectRatio="none">
      <defs>
        <linearGradient id="cityscape" x1="0" y1="0" x2="0" y2="1">
          <stop offset="0" stop-color="#6f8aa6"/>
          <stop offset="0.35" stop-color="#b9c4cf"/>
          <stop offset="0.55" stop-color="#e9c6a8"/>
          <stop offset="0.62" stop-color="#5a4a4f"/>
          <stop offset="0.7" stop-color="#c9c6c8"/>
          <stop offset="0.82" stop-color="#ffffff"/>
        </linearGradient>
      </defs>
      <polygon class="corner-accent" points="0,0 130,0 0,250" fill="var(--brand-red)"/>
      <polygon class="corner-stripe" points="130,0 185,0 0,360 0,262" fill="var(--stripe-grey)"/>
      <polygon class="divider-stripe" points="1118,0 1160,0 1013,435 970,435" fill="var(--stripe-grey)"/>
      <polygon class="contact-panel" points="0,630 62,630 150,435 1013,435 1160,0 1212,0 1068,432 1185,682 0,682" fill="var(--brand-red)"/>
      <polygon class="photo-area" role="img" aria-label="Foto: Hängebrücke über einem Fluss vor einer Großstadt-Skyline bei Abenddämmerung"
        points="1222,0 1820,0 1820,682 1197,682 1080,432" fill="url(#cityscape)"/>
    </svg>

    <div class="brand">Nordhaus Immobilien</div>
    <div class="brand__rule"></div>
    <div class="tagline">WIR ERLEDIGEN IHRE HAUS-AUFGABEN</div>

    <svg class="contact__phone-icon" viewBox="0 0 24 24" aria-hidden="true">
      <path fill="var(--phone-pink)" d="M6.6 10.8c1.4 2.8 3.8 5.1 6.6 6.6l2.2-2.2c.3-.3.7-.4 1-.2 1.1.4 2.3.6 3.6.6.6 0 1 .4 1 1V20c0 .6-.4 1-1 1C10.6 21 3 13.4 3 4c0-.6.4-1 1-1h3.5c.6 0 1 .4 1 1 0 1.3.2 2.5.6 3.6.1.3 0 .7-.2 1l-2.3 2.2z"/>
    </svg>
    <div class="contact__phone">0391 480 27 63</div>

    <svg class="contact__web-icon" viewBox="0 0 28 28" aria-hidden="true">
      <circle cx="14" cy="14" r="14" fill="var(--phone-pink)"/>
      <g fill="none" stroke="var(--brand-red)" stroke-width="1.4">
        <circle cx="14" cy="14" r="8"/>
        <ellipse cx="14" cy="14" rx="3.6" ry="8"/>
        <line x1="6" y1="14" x2="22" y2="14"/>
        <line x1="7.5" y1="10" x2="20.5" y2="10"/>
        <line x1="7.5" y1="18" x2="20.5" y2="18"/>
      </g>
    </svg>
    <div class="contact__web">www.nordhaus-verwaltung.de</div>

    <div class="services">
      <p class="services__title">Immobilienverwaltung<br>und -vermarktung</p>
      <p class="services__claim">mit Know-how aus Leidenschaft.</p>
    </div>
  </section>
</body>
</html>
```